Business Cards - New Logo Rebranding

Hello We know have a red and blue logo and are looking to create new cards. We are looking for the best creativity of the new logo merged with some of the existing artwork provided.

Target Market(s)

Realtors

Industry/Entity Type

Real Estate

Contact Information for Business Card

New logo with rebranded colors

Requirements
Must have
• Creative use of the new logo

```html
<!DOCTYPE html>
<html lang="en">
<head>
<meta charset="UTF-8">
<title>Summit Crest Inspection Professionals – Business Cards</title>
<link href="https://fonts.googleapis.com/css2?family=Exo+2:wght@500;700&family=Oswald:wght@500;600&display=swap" rel="stylesheet">
<style>
  :root{
    --bg:#2a2a2c;
    --card:#b9babc;
    --red:#e0404a;
    --blue:#2a86d6;
    --ink:#2b2b2e;
    --badge-red:#b8323c;
    --badge-gold:#c9a23a;
    --badge-silver:#9a9890;
    --badge-navy:#2f3f7a;
  }
  *{box-sizing:border-box;margin:0;padding:0}
  html,body{width:1200px;height:900px;overflow:hidden;background:var(--bg)}
  .canvas{position:relative;width:1200px;height:900px}
  .card{position:absolute;width:740px;height:420px;background:var(--card);box-shadow:0 10px 24px rgba(0,0,0,.45);overflow:hidden}
  .card--back{left:150px;top:22px}
  .card--front{left:310px;top:458px}

  .wide{font-family:"Exo 2",sans-serif;font-weight:500;letter-spacing:1.5px;text-transform:uppercase}
  .cond{font-family:"Oswald",sans-serif;font-weight:500;text-transform:uppercase;color:var(--ink)}

  /* back */
  .back__headline{position:absolute;left:40px;top:36px;color:var(--red);font-size:19px;padding-bottom:8px;border-bottom:2px solid var(--blue);width:410px;white-space:nowrap}
  .back__sub{position:absolute;left:40px;top:78px;color:var(--red);font-size:17px}
  .reasons{position:absolute;left:40px;top:112px;width:440px;list-style:none}
  .reasons li{display:flex;align-items:center;gap:9px;font-size:17px;line-height:27px;white-space:nowrap}
  .reasons svg{flex:none}
  .badges{position:absolute;left:44px;top:345px;display:flex;align-items:center;gap:20px}
  .badge{width:54px;height:54px;border-radius:50%}
  .badge--red{background:var(--badge-red);border:4px solid #e6e6e6}
  .badge--gold{background:var(--badge-navy);border:5px solid var(--badge-gold)}
  .badge--silver{background:#d8d6cc;border:5px solid var(--badge-silver)}
  .badge--pilot{width:110px;height:40px;border-radius:20px 6px 6px 20px;background:var(--badge-navy)}
  .badge--stars{width:70px;height:34px;border-radius:4px;background:var(--red)}
  .badge--ring{width:34px;height:34px;border-radius:50%;border:5px solid var(--blue);background:transparent}

  .brand{position:absolute;display:flex;flex-direction:column;align-items:center}
  .brand__mark{width:110px;height:110px;border-radius:50%;background:var(--red);margin-bottom:10px}
  .brand__name{font-family:"Exo 2",sans-serif;font-weight:700;font-size:30px;color:var(--blue);letter-spacing:1px;text-transform:uppercase;line-height:1;white-space:nowrap}
  .brand__tag{font-family:"Exo 2",sans-serif;font-weight:500;font-size:11px;color:var(--blue);letter-spacing:1px;text-transform:uppercase;border-top:2px solid var(--blue);margin-top:5px;padding-top:3px;white-space:nowrap}
  .card--back .brand{right:28px;top:40px}
  .card--front .brand{right:40px;top:34px}

  /* front */
  .person{position:absolute;left:44px;top:120px;width:300px;border-bottom:2px solid var(--blue);padding-bottom:12px}
  .person__name{color:var(--red);font-size:30px;font-weight:500}
  .person__title{font-size:20px;margin-top:2px}
  .contacts{position:absolute;left:44px;top:238px;list-style:none}
  .contacts li{display:flex;align-items:center;gap:12px;font-size:19px;line-height:28px}
  .contacts svg{flex:none}
  .services{position:absolute;left:44px;right:44px;bottom:26px;border-top:2px solid var(--blue);padding-top:8px;font-size:22px;letter-spacing:.5px}
  .services .dot{color:var(--red);margin:0 8px}
</style>
</head>
<body>
<div class="canvas">

  <section class="card card--back">
    <h2 class="back__headline wide">California's #1 Inspection Company!</h2>
    <p class="back__sub wide">Why choose Summit Crest...</p>
    <ul class="reasons cond">
      <li><svg width="15" height="13" viewBox="0 0 16 14"><path d="M1 7l5 5L15 1" fill="none" stroke="var(--red)" stroke-width="3"/></svg>Performing inspections since 1984</li>
      <li><svg width="15" height="13" viewBox="0 0 16 14"><path d="M1 7l5 5L15 1" fill="none" stroke="var(--red)" stroke-width="3"/></svg>HomeCert certified master / professional inspectors®</li>
      <li><svg width="15" height="13" viewBox="0 0 16 14"><path d="M1 7l5 5L15 1" fill="none" stroke="var(--red)" stroke-width="3"/></svg>500,000+ inspections completed statewide</li>
      <li><svg width="15" height="13" viewBox="0 0 16 14"><path d="M1 7l5 5L15 1" fill="none" stroke="var(--red)" stroke-width="3"/></svg>Request of repairs pricer report</li>
      <li><svg width="15" height="13" viewBox="0 0 16 14"><path d="M1 7l5 5L15 1" fill="none" stroke="var(--red)" stroke-width="3"/></svg>90-day inspection guarantees</li>
      <li><svg width="15" height="13" viewBox="0 0 16 14"><path d="M1 7l5 5L15 1" fill="none" stroke="var(--red)" stroke-width="3"/></svg>AeroCert drone licensed roof inspectors upon request</li>
      <li><svg width="15" height="13" viewBox="0 0 16 14"><path d="M1 7l5 5L15 1" fill="none" stroke="var(--red)" stroke-width="3"/></svg>5,000+ 5-star reviews on ReviewHub &amp; StarList</li>
    </ul>
    <div class="badges">
      <span class="badge badge--red"></span>
      <span class="badge badge--gold"></span>
      <span class="badge badge--silver"></span>
      <span class="badge badge--pilot"></span>
      <span class="badge badge--stars"></span>
      <span class="badge badge--ring"></span>
    </div>
    <div class="brand">
      <span class="brand__mark"></span>
      <span class="brand__name">Summit Crest</span>
      <span class="brand__tag">Inspection Professionals</span>
    </div>
  </section>

  <section class="card card--front">
    <div class="brand">
      <span class="brand__mark"></span>
      <span class="brand__name">Summit Crest</span>
      <span class="brand__tag">Inspection Professionals</span>
    </div>
    <div class="person">
      <h1 class="person__name wide">Dana Whitfield</h1>
      <p class="person__title cond">Certified Mold Inspector</p>
    </div>
    <ul class="contacts cond">
      <li><svg width="16" height="20" viewBox="0 0 16 20"><rect x="3" y="1" width="10" height="18" rx="2" fill="none" stroke="var(--red)" stroke-width="2"/></svg>555.014.2290</li>
      <li><svg width="16" height="18" viewBox="0 0 16 18"><path d="M3 2l3 0 1 4-2 1c1 3 3 5 5 6l1-2 4 1v3c-6 1-13-6-12-13z" fill="var(--red)"/></svg>800.555.0176</li>
      <li><svg width="16" height="14" viewBox="0 0 16 14"><rect x="1" y="2" width="14" height="10" fill="var(--red)"/><path d="M1 2l7 6 7-6" fill="none" stroke="var(--card)" stroke-width="1.5"/></svg>dana@summitcrestinspect.com</li>
      <li><svg width="16" height="16" viewBox="0 0 16 16"><circle cx="8" cy="8" r="6.5" fill="none" stroke="var(--red)" stroke-width="1.5"/><path d="M1.5 8h13M8 1.5c-3 3.5-3 9.5 0 13M8 1.5c3 3.5 3 9.5 0 13" fill="none" stroke="var(--red)" stroke-width="1.2"/></svg>www.summitcrestinspect.com</li>
    </ul>
    <p class="services cond">Home<span class="dot">•</span>Sewer<span class="dot">•</span>Mold<span class="dot">•</span>Commercial<span class="dot">•</span>Termite<span class="dot">•</span>Roof</p>
  </section>

</div>
</body>
</html>
```